Bref créative
Dale's Furniture
Stationary, Letterhead, Business Cards, Envelopes
I need single sided standard sized Business Card [3.5" x 2"]
Similar to Logo Font
Bright & Fun-filled
Dale's Furniture and Appliances
4817 W. Corvel Ave.
Chicago IL 60688
Dalesfurnitureandappliances@quillmail.example
www.dalesfurnitureandapplianes.example
Current Logo
Black and White Version

```html
<!DOCTYPE html>
<html lang="en">
<head>
<meta charset="utf-8">
<title>Dale's Furniture – Business Cards</title>
<link href="https://fonts.googleapis.com/css2?family=Tinos:wght@400;700&display=swap" rel="stylesheet">
<style>
  :root {
    --backdrop: #e9dcc6;
    --card-white: #ffffff;
    --card-white-shade: #e6e6e6;
    --brand-red: #d7141a;
    --brand-red-deep: #a50c10;
    --brand-red-glow: #f04a4a;
    --ink: #1a1a1a;
    --ink-soft: #3a3a3a;
    --card-black: #1b1b1b;
    --card-black-glow: #4a4a4a;
    --rule: #9a9a9a;
  }
  * { box-sizing: border-box; margin: 0; padding: 0; }
  html, body {
    width: 1200px; height: 718px; overflow: hidden;
    background: var(--backdrop);
    font-family: "Tinos", "Times New Roman", serif;
  }
  .canvas { position: relative; width: 1200px; height: 718px; }

  .card {
    position: absolute;
    border-radius: 16px;
    overflow: hidden;
    box-shadow: 0 6px 14px rgba(0,0,0,.28);
  }

  /* Front card */
  .card--front {
    left: 330px; top: 34px; width: 600px; height: 310px;
    background: linear-gradient(180deg, var(--card-white) 0%, var(--card-white) 55%, var(--card-white-shade) 100%);
  }
  .card--front .brand {
    position: absolute; left: 36px; top: 100px; width: 200px;
    display: flex; align-items: center; gap: 8px;
  }
  .brand-mark { width: 16px; height: 16px; flex: none; }
  .card--front .brand-mark { background: var(--brand-red); }
  .brand-name { font-weight: 700; line-height: 1; white-space: nowrap; }
  .card--front .brand-name { font-size: 25px; color: var(--ink); }

  .divider {
    position: absolute; left: 252px; top: 94px; width: 1px; height: 116px;
    background: var(--rule);
  }
  .contact {
    position: absolute; left: 266px; top: 94px;
    font-size: 13px; line-height: 16px; color: var(--ink-soft);
    list-style: none; white-space: nowrap;
  }
  .contact .gap { margin-top: 16px; }
  .contact .label { color: var(--brand-red); display: inline-block; width: 14px; }

  .swoosh { position: absolute; left: 0; bottom: 0; width: 600px; height: 110px; }

  /* Back cards */
  .card--back {
    top: 377px; height: 307px;
    display: flex; align-items: center; justify-content: center;
  }
  .card--red {
    left: 43px; width: 528px;
    background: radial-gradient(ellipse at 50% 38%, var(--brand-red-glow) 0%, var(--brand-red) 45%, var(--brand-red-deep) 100%);
  }
  .card--black {
    left: 624px; width: 535px;
    background: radial-gradient(ellipse at 50% 35%, var(--card-black-glow) 0%, var(--card-black) 70%);
  }
  .card--back .brand { display: flex; align-items: center; gap: 10px; margin-top: -30px; }
  .card--back .brand-name { font-size: 34px; color: #ffffff; }
  .card--back .brand-mark { width: 20px; height: 20px; background: #ffffff; }
</style>
</head>
<body>
<main class="canvas">

  <section class="card card--front" aria-label="Business card front">
    <div class="brand">
      <span class="brand-mark"></span>
      <span class="brand-name">Dale's Furniture</span>
    </div>
    <div class="divider"></div>
    <ul class="contact">
      <li>4817 W. Corvel Ave.</li>
      <li>Chicago IL 60688</li>
      <li class="gap"><span class="label">P</span>: 555-276-0142</li>
      <li><span class="label">F</span>: 555-276-0187</li>
      <li><span class="label">E</span>: Dalesfurnitureandappliances@quillmail.example</li>
      <li>www.dalesfurnitureandapplianes.example</li>
    </ul>
    <svg class="swoosh" viewBox="0 0 600 110" preserveAspectRatio="none">
      <path d="M0 60 C150 110 330 62 600 50 L600 110 L0 110 Z" fill="#111"/>
      <path d="M0 48 C160 100 330 60 600 40 L600 54 C330 74 160 112 0 66 Z" fill="var(--brand-red)"/>
      <path d="M0 72 C170 118 360 80 600 66 L600 110 L0 110 Z" fill="#2a2a2a"/>
    </svg>
  </section>

  <section class="card card--back card--red" aria-label="Business card back, red">
    <div class="brand">
      <span class="brand-mark"></span>
      <span class="brand-name">Dale's Furniture</span>
    </div>
  </section>

  <section class="card card--back card--black" aria-label="Business card back, black">
    <div class="brand">
      <span class="brand-mark"></span>
      <span class="brand-name">Dale's Furniture</span>
    </div>
  </section>

</main>
</body>
</html>
```